Zielgruppe
Wir vermieten Köche und Küchenhilfen an unsere Kunden. Die Visitenkarten sind sowohl für potentielle Neukunden als auch potentielle neue Mitarbeitern.
Aufgabenstellung
Unsere Visitenkarten sollen modern sein ohne zu voll zu wirken.
Auf ihr enthalten sollen sein: Logo, Name, Position, Telefonnr (Festnetz und Mobil), Adresse, Email und Logo.
Ein kurzer, knapper Motivationsspruch wäre auch schön.

```html
<!DOCTYPE html>
<html lang="de">
<head>
<meta charset="utf-8">
<title>Tarvo Catering – Visitenkarte</title>
<link rel="stylesheet" href="https://fonts.googleapis.com/css2?family=Fira+Sans:wght@400;500;600&display=swap">
<style>
  :root {
    --stage: #2b2b2b;
    --paper: #ffffff;
    --ink: #3c3c3c;
    --grey: #808080;
    --grey-dark: #474747;
    --orange: #e8631c;
  }
  * { margin: 0; padding: 0; box-sizing: border-box; }
  html, body { width: 1200px; height: 932px; overflow: hidden; }
  body {
    background: var(--stage);
    font-family: "Fira Sans", Arial, sans-serif;
    position: relative;
  }
  .card {
    position: absolute;
    top: 97px;
    width: 451px;
    height: 697px;
    background: var(--paper);
    overflow: hidden;
  }
  .card--front { left: 90px; }
  .card--back { left: 619px; }
  .card__band {
    position: absolute;
    left: 0;
    right: 0;
    height: 160px;
  }
  .card--front .card__band {
    top: 0;
    background: linear-gradient(to bottom, var(--grey) 0%, var(--grey-dark) 75%, var(--orange) 100%);
  }
  .card--back .card__band {
    bottom: 0;
    height: 165px;
    background: linear-gradient(to top, var(--grey) 0%, var(--grey-dark) 75%, var(--orange) 100%);
  }
  .brand {
    position: absolute;
    left: 0; right: 0;
    display: flex;
    flex-direction: column;
    align-items: center;
  }
  .brand__dot { border-radius: 50%; background: var(--orange); }
  .brand__name {
    font-weight: 500;
    color: var(--grey-dark);
    text-transform: uppercase;
    letter-spacing: 0.12em;
    white-space: nowrap;
  }
  .card--front .brand { top: 265px; gap: 26px; }
  .card--front .brand__dot { width: 100px; height: 100px; }
  .card--front .brand__name { font-size: 34px; }
  .card--back .brand { top: 44px; gap: 16px; }
  .card--back .brand__dot { width: 56px; height: 56px; }
  .card--back .brand__name { font-size: 19px; }
  .tagline {
    position: absolute;
    left: 0; right: 0;
    top: 633px;
    text-align: center;
    color: var(--orange);
    font-weight: 600;
    font-size: 19px;
    font-variant: small-caps;
    letter-spacing: 0.02em;
  }
  .contact {
    position: absolute;
    left: 0; right: 0;
    top: 215px;
    text-align: center;
    color: var(--ink);
    font-variant: small-caps;
  }
  .contact__name { font-size: 30px; font-weight: 600; letter-spacing: 0.03em; }
  .contact__role { font-size: 19px; margin-top: 6px; letter-spacing: 0.04em; }
  .contact__address { font-size: 20px; line-height: 25px; margin-top: 36px; letter-spacing: 0.04em; }
  .contact__phones {
    margin: 24px auto 0;
    display: grid;
    grid-template-columns: auto auto;
    column-gap: 10px;
    justify-content: center;
    text-align: left;
    color: var(--orange);
    font-size: 20px;
    line-height: 25px;
    letter-spacing: 0.04em;
  }
  .contact__email { font-size: 16px; margin-top: 24px; letter-spacing: 0.08em; text-transform: uppercase; }
  .website {
    position: absolute;
    left: 66px;
    top: 635px;
    color: #fff;
    font-size: 17px;
    letter-spacing: 0.06em;
    text-transform: uppercase;
  }
</style>
</head>
<body>
  <section class="card card--front">
    <div class="card__band" role="img" aria-label="Dekoratives Band in Grau und Orange"></div>
    <div class="brand">
      <span class="brand__dot"></span>
      <span class="brand__name">Tarvo Catering</span>
    </div>
    <p class="tagline">Event – Personal – Ihr Spezialist</p>
  </section>

  <section class="card card--back">
    <div class="card__band" role="img" aria-label="Dekoratives Band in Grau und Orange"></div>
    <div class="brand">
      <span class="brand__dot"></span>
      <span class="brand__name">Tarvo Catering</span>
    </div>
    <div class="contact">
      <p class="contact__name">VORNAME NACHNAME</p>
      <p class="contact__role">Geschäftsführer</p>
      <p class="contact__address">Talstraße 16<br>61138 Niederau</p>
      <div class="contact__phones">
        <span>Festnetz:</span><span>0176 / 4281937</span>
        <span>Mobile:</span><span>0176 / 4281937</span>
      </div>
      <p class="contact__email">info@tarvo-catering.de</p>
    </div>
    <p class="website">www.tarvo-catering.de</p>
  </section>
</body>
</html>
```